business card - Helicopter Flight Services, Flight School, etc.

We need a business card design for a new helicopter service.

We offer Helicopter Flight Services, Aerial Filming & Photography, Flight School, and Helicopter Tours. In that order.

Summit BladeLine, Inc.
Harold Tebbets
SummitBladeline@Mailvane.com
555-014-2786

Based at the Corvell Airport in Van Nuys, CA. The final design should communicate integrity and safety. Pictures or logos at your discretion.

Card back side - surprise me.

```html
<!DOCTYPE html>
<html lang="en">
<head>
<meta charset="utf-8">
<title>Summit BladeLine, Inc. — Business Card</title>
<link rel="stylesheet" href="https://fonts.googleapis.com/css2?family=Quicksand:wght@700&family=Open+Sans:wght@300;400&display=swap">
<style>
  :root {
    --stage: #e6e6ea;
    --violet: #3f3585;
    --violet-light: #544a9c;
    --paper: #f7f7f8;
    --ink: #222227;
    --ink-soft: #55555c;
    --white: #ffffff;
  }
  * { margin: 0; padding: 0; box-sizing: border-box; }
  html, body {
    width: 1200px; height: 900px; overflow: hidden;
    background: var(--stage);
  }
  .sheet {
    width: 1200px; height: 900px;
    display: flex; flex-direction: column;
    align-items: center; justify-content: center; gap: 70px;
  }
  .card {
    width: 600px; height: 343px;
    border-radius: 3px;
    overflow: hidden;
    box-shadow: 0 8px 24px rgba(0,0,0,0.18);
    position: relative;
  }
  .card-front {
    background: radial-gradient(circle at 60% 55%, var(--violet-light), var(--violet) 75%);
    display: flex; align-items: center; justify-content: center;
  }
  .wordmark {
    display: flex; align-items: center; gap: 14px;
    font-family: "Quicksand", sans-serif; font-weight: 700;
    color: var(--white);
  }
  .wordmark-dot {
    width: 18px; height: 18px; border-radius: 50%;
    background: var(--white);
  }
  .card-front .wordmark { font-size: 40px; }
  .card-back { display: flex; }
  .back-info {
    width: 56%; background: var(--paper);
    padding: 118px 0 0 40px;
  }
  .company-name {
    font-family: "Quicksand", sans-serif; font-weight: 700;
    font-size: 25px; color: var(--ink); letter-spacing: -0.2px;
  }
  .person-name {
    font-family: "Open Sans", sans-serif; font-weight: 300;
    font-size: 15px; color: var(--ink-soft); margin: 4px 0 10px;
  }
  .contact-line {
    display: flex; align-items: center; gap: 9px;
    font-family: "Open Sans", sans-serif; font-weight: 300;
    font-size: 14px; color: var(--ink-soft); line-height: 1.65;
  }
  .contact-line svg { width: 9px; height: 9px; fill: var(--ink-soft); flex: none; }
  .back-brand {
    width: 44%;
    background: radial-gradient(circle at 50% 50%, var(--violet-light), var(--violet) 80%);
    display: flex; align-items: center; justify-content: center;
  }
  .back-brand .wordmark { font-size: 21px; gap: 10px; }
  .back-brand .wordmark-dot { width: 12px; height: 12px; }
</style>
</head>
<body>
<main class="sheet">
  <section class="card card-front" aria-label="Card front">
    <div class="wordmark"><span class="wordmark-dot"></span><span>Summit BladeLine</span></div>
  </section>

  <section class="card card-back" aria-label="Card back">
    <div class="back-info">
      <h1 class="company-name">Summit BladeLine, Inc.</h1>
      <p class="person-name">Harold Tebbets</p>
      <p class="contact-line">
        <svg viewBox="0 0 10 10" aria-hidden="true"><path d="M2 0.5 L4 2.8 L3 4 Q4.2 6 6 7 L7.2 6 L9.5 8 L8 9.7 Q4 9.5 0.3 2 Z"/></svg>
        555-014-2786
      </p>
      <p class="contact-line">
        <svg viewBox="0 0 10 10" aria-hidden="true"><path d="M0.5 2 H9.5 V8.5 H0.5 Z M1.3 2.6 L5 5.6 L8.7 2.6" fill="none" stroke="#55555c" stroke-width="1"/></svg>
        SummitBladeline@Mailvane.com
      </p>
    </div>
    <div class="back-brand">
      <div class="wordmark"><span class="wordmark-dot"></span><span>Summit BladeLine</span></div>
    </div>
  </section>
</main>
</body>
</html>
```